Plumbing company needs Business Card Design

Hi I need business card design based on logo which I uploaded. Its plumbing and heating company called Wodorex Usługi Hydrauliczno-Gazowe. I want to see on my card motto of my company which is "...od wymiany uszczelki po wymiane łazienki.", my phone number, name, and website: 608472915, Marek Kowalczyk, info@wodorex-example.org, www.wodorex-example.org
I want to see logos of companys which I'm approved installer (Termovo) (Le Varnoux) (Kelm) (Ostra).
I want new creative look of business card. I like rounded corners.
Any questions please send message.
Thanks for intrest.
Industry/Entity Type
Business
Contact Information for Business Card
Marek Kowalczyk
608 472 915
info@wodorex-example.org
www.wodorex-example.org
...od wymiany uszczelki po wymiane łazienki.

```html
<!DOCTYPE html>
<html lang="pl">
<head>
<meta charset="utf-8">
<title>Wodorex – wizytówka</title>
<link rel="stylesheet" href="https://fonts.googleapis.com/css2?family=Anton&family=Roboto+Condensed:wght@400;700;800&display=swap">
<style>
  :root {
    --stage: #d8d4cf;
    --card: #ffffff;
    --card-shade: #eeeeef;
    --brand-red: #e0202e;
    --brand-blue: #233a8f;
    --brand-yellow: #ffe600;
    --pattern-light: #f1f1f3;
    --pattern-dark: #d7d8dd;
  }
  * { box-sizing: border-box; margin: 0; padding: 0; }
  html, body {
    width: 1200px;
    height: 694px;
    overflow: hidden;
    background: var(--stage);
  }
  .canvas {
    position: relative;
    width: 1200px;
    height: 694px;
  }
  .card {
    position: absolute;
    top: 191px;
    width: 540px;
    height: 312px;
    border-radius: 18px;
    overflow: hidden;
    background: linear-gradient(135deg, var(--card) 0%, var(--card-shade) 100%);
    box-shadow: 0 10px 26px rgba(0,0,0,0.18);
  }
  .card--front { left: 40px; }
  .card--back { left: 620px; }

  /* front */
  .card__pattern {
    position: absolute;
    inset: 0;
    background: linear-gradient(160deg, var(--pattern-light) 0%, var(--pattern-dark) 100%);
  }
  .brand {
    position: absolute;
    left: 48px;
    top: 70px;
    width: 444px;
  }
  .brand__row {
    display: flex;
    align-items: center;
    gap: 16px;
  }
  .brand__square {
    flex: none;
    width: 92px;
    height: 92px;
    border-radius: 14px;
    background: var(--brand-yellow);
  }
  .brand__name {
    font-family: "Anton", sans-serif;
    font-size: 84px;
    line-height: 1;
    color: var(--brand-red);
  }
  .brand__services {
    margin-top: 4px;
    padding-left: 108px;
    font-family: "Roboto Condensed", sans-serif;
    font-weight: 400;
    font-size: 22px;
    line-height: 1.2;
    color: var(--brand-blue);
  }
  .brand__motto {
    margin-top: 8px;
    font-family: "Roboto Condensed", sans-serif;
    font-weight: 800;
    font-size: 24px;
    line-height: 1.2;
    color: var(--brand-blue);
  }

  /* back */
  .contact {
    position: absolute;
    left: 50px;
    top: 48px;
    width: 440px;
  }
  .contact__name {
    font-family: "Anton", sans-serif;
    font-size: 44px;
    line-height: 1.1;
    color: var(--brand-red);
    letter-spacing: 0.5px;
  }
  .contact__motto {
    margin-top: 4px;
    font-family: "Roboto Condensed", sans-serif;
    font-weight: 800;
    font-size: 17px;
    line-height: 1.2;
    color: var(--brand-blue);
  }
  .contact__rule {
    height: 2px;
    background: var(--brand-blue);
    margin: 6px 0;
  }
  .contact__phone {
    font-family: "Anton", sans-serif;
    font-size: 76px;
    line-height: 1.1;
    color: var(--brand-red);
    letter-spacing: 1px;
  }
  .contact__links {
    display: flex;
    align-items: center;
    justify-content: space-between;
    font-family: "Roboto Condensed", sans-serif;
    font-weight: 800;
    font-size: 17px;
    line-height: 1.2;
    color: var(--brand-blue);
  }
  .contact__divider { color: var(--brand-red); font-weight: 400; }
</style>
</head>
<body>
  <main class="canvas">
    <section class="card card--front" aria-label="Przód wizytówki">
      <div class="card__pattern" role="img" aria-label="Delikatny powtarzający się wzór z emblematem hydraulika w odcieniach szarości"></div>
      <div class="brand">
        <div class="brand__row">
          <span class="brand__square" aria-hidden="true"></span>
          <span class="brand__name">Wodorex</span>
        </div>
        <p class="brand__services">Usługi Hydrauliczno-Gazowe</p>
        <p class="brand__motto">wymiany uszczelki po wymiane łazienki.</p>
      </div>
    </section>

    <section class="card card--back" aria-label="Tył wizytówki">
      <div class="contact">
        <h1 class="contact__name">Marek Kowalczyk</h1>
        <p class="contact__motto">wymiany uszczelki po wymiane łazienki.</p>
        <div class="contact__rule"></div>
        <p class="contact__phone">608 472 915</p>
        <div class="contact__rule"></div>
        <p class="contact__links">
          <span class="contact__email">info@wodorex-example.org</span>
          <span class="contact__divider">/</span>
          <span class="contact__web">www.wodorex-example.org</span>
        </p>
      </div>
    </section>
  </main>
</body>
</html>
```